Visitenkarten-Design für Anbieter von Softwarelösungen rund ums Bargeld
Unser Favorit war gleich beim 1. Entwurf mit dabei. Schön war vor allem, dass uns gleich 3 verschiedene Farbvarianten angeboten wurden. Daher bedurfte es auch keinerlei Anpassungen von unserer Seite. Herzlichen Dank!
Zielgruppe
Unsere Unternehmensgruppe, bestehend aus mehreren Tochterunternehmen, ist ein führender europäischer Anbieter für Softwarelösungen rund ums Bargeld.
Unsere Lösungen unterstützen Handelsunternehmen, Wertdienstleister und Finanzinstitute bei der Erfassung und Nachverfolgung von Zahlungsströmen im Bargeldkreislauf (Cash Management + Track & Trace). Bargeldmanagementprozesse werden durch unsere Produkte bei unseren Kunden optimiert, Verwaltungs-, Prozess- und Personalkosten gesenkt: Für mehr Sicherheit, Effizienz und Transparenz.
Es ist wahrscheinlich, dass wir zukünftig mittels Zukäufen über unsere derzeitigen Tätigkeitsfelder hinaus wachsen. Neben Cash wird die (Werte-)Logistik bzw. Logistik generell eine Rolle spielen. Auch unter der Maßgabe, dass zukünftig nur noch Services (statt Verkauf von Software) angeboten werden.
Der Fokus wird sich weiterhin primär auf Geschäftskunden beschränken: Wir helfen Unternehmen, effizienter zu werden.
www.digital.korven-beispiel.eu
Aufgabenstellung
Die Schreibweise unseres Namens sieht wie folgt aus: 'KORVEN | Digital Solutions'
Die Farbcodes des Logo sind in der Datei abgebildet.
Als ergänzende Farben nutzen wir aktuell ein Türkis (CMYK: 53/23/21/0 | #86ACBA) und ein Dunkelgrau (CMYK: 77/62/38/21 | #44546A). Diese dürfen gerne mit verwendet werden.

```html
<!DOCTYPE html>
<html lang="en">
<head>
<meta charset="utf-8">
<title>KORVEN | Digital Solutions – Business Card</title>
<link href="https://fonts.googleapis.com/css2?family=Montserrat:wght@300;400;500;600;700&display=swap" rel="stylesheet">
<style>
  :root {
    --teal: #7aa5b8;
    --teal-light: #86acba;
    --slate: #44546a;
    --paper: #ffffff;
    --backdrop: #eceef0;
    --map-tint: #f2f4f5;
  }
  * { margin: 0; padding: 0; box-sizing: border-box; }
  html, body { width: 1000px; height: 1200px; overflow: hidden; }
  body {
    background: var(--backdrop);
    font-family: "Montserrat", sans-serif;
    position: relative;
  }
  .card {
    position: absolute;
    left: 100px;
    width: 800px;
    height: 480px;
    background: var(--paper);
    overflow: hidden;
    box-shadow: 0 4px 18px rgba(40, 55, 70, 0.10);
  }
  .card--front { top: 90px; }
  .card--back { top: 640px; }

  .world-map {
    position: absolute;
    background: radial-gradient(ellipse at center, var(--map-tint) 0%, var(--map-tint) 55%, rgba(242,244,245,0) 80%);
  }
  .card--front .world-map { left: 330px; top: 60px; width: 400px; height: 300px; }
  .card--back .world-map { left: 360px; top: 70px; width: 420px; height: 310px; }

  .holder { position: absolute; left: 88px; top: 90px; }
  .holder__name {
    font-size: 32px;
    color: var(--slate);
    letter-spacing: 0.5px;
    line-height: 1;
  }
  .holder__first { font-weight: 600; }
  .holder__last { font-weight: 300; }
  .holder__role {
    margin-top: 8px;
    font-size: 15px;
    font-weight: 400;
    color: var(--teal-light);
    letter-spacing: 0.3px;
  }
  .holder__rule {
    margin-top: 8px;
    width: 40px;
    height: 3px;
    background: var(--slate);
  }

  .brand {
    position: absolute;
    display: flex;
    align-items: center;
    gap: 16px;
  }
  .card--front .brand { left: 450px; top: 82px; }
  .card--back .brand { left: 440px; top: 206px; }
  .brand__dot {
    width: 52px;
    height: 52px;
    border-radius: 50%;
    background: var(--teal);
  }
  .brand__text {
    color: var(--teal);
    font-weight: 600;
    line-height: 1;
  }
  .brand__name { font-size: 40px; letter-spacing: 1px; }
  .brand__tag { font-size: 14px; margin-top: 6px; letter-spacing: 0.4px; }

  .contacts {
    position: absolute;
    left: 80px;
    top: 225px;
    list-style: none;
  }
  .contacts__item {
    display: flex;
    align-items: center;
    height: 24px;
    margin-bottom: 33px;
    font-size: 17px;
    font-weight: 500;
    color: var(--teal);
    letter-spacing: 0.2px;
  }
  .contacts__icon { width: 18px; height: 18px; fill: var(--slate); }
  .contacts__bar {
    width: 3px;
    height: 24px;
    background: var(--slate);
    margin: 0 18px 0 12px;
  }

  .arrow-band { position: absolute; left: 0; bottom: 0; }

  .website {
    position: absolute;
    right: 112px;
    bottom: 40px;
    font-size: 16px;
    font-weight: 400;
    color: var(--slate);
    letter-spacing: 0.3px;
  }
</style>
</head>
<body>

  <section class="card card--front" aria-label="Business card front">
    <div class="world-map" role="img" aria-label="Faint dotted world map in the background"></div>

    <div class="holder">
      <p class="holder__name"><span class="holder__first">LENA</span> <span class="holder__last">HARTWIG</span></p>
      <p class="holder__role">GENERAL MANAGER</p>
      <div class="holder__rule"></div>
    </div>

    <div class="brand">
      <span class="brand__dot"></span>
      <div class="brand__text">
        <div class="brand__name">KORVEN</div>
        <div class="brand__tag">DIGITAL SOLUTIONS</div>
      </div>
    </div>

    <ul class="contacts">
      <li class="contacts__item">
        <svg class="contacts__icon" viewBox="0 0 24 24" aria-hidden="true"><path d="M6.6 10.8a15.1 15.1 0 0 0 6.6 6.6l2.2-2.2a1 1 0 0 1 1-.25 11.4 11.4 0 0 0 3.6.57 1 1 0 0 1 1 1V20a1 1 0 0 1-1 1A17 17 0 0 1 3 4a1 1 0 0 1 1-1h3.5a1 1 0 0 1 1 1c0 1.25.2 2.45.57 3.6a1 1 0 0 1-.25 1z"/></svg>
        <span class="contacts__bar"></span>
        <span>+000-123-456-789</span>
      </li>
      <li class="contacts__item">
        <svg class="contacts__icon" viewBox="0 0 24 24" aria-hidden="true"><path d="M2 5h20v14H2z M2 5l10 8 10-8" fill-rule="evenodd"/><path d="M2 5l10 7 10-7" fill="none" stroke="#fff" stroke-width="1.6"/></svg>
        <span class="contacts__bar"></span>
        <span>kontakt@postfach-muster.eu</span>
      </li>
      <li class="contacts__item">
        <svg class="contacts__icon" viewBox="0 0 24 24" aria-hidden="true"><path d="M12 2a7 7 0 0 0-7 7c0 5 7 13 7 13s7-8 7-13a7 7 0 0 0-7-7zm0 9.5A2.5 2.5 0 1 1 12 6.5a2.5 2.5 0 0 1 0 5z"/></svg>
        <span class="contacts__bar"></span>
        <span>Suite # 210 Lindenweg 8&nbsp; Musterstadt Germany</span>
      </li>
    </ul>

    <svg class="arrow-band" width="720" height="90" viewBox="0 0 720 90" aria-hidden="true">
      <polygon points="0,6 595,6 638,48 600,90 0,90" fill="var(--teal)"/>
      <polygon points="620,6 655,6 700,48 655,90 582,90 627,48" fill="var(--slate)"/>
      <polygon points="462,90 500,60 600,60 570,90" fill="var(--teal)"/>
    </svg>
  </section>

  <section class="card card--back" aria-label="Business card back">
    <div class="world-map" role="img" aria-label="Faint dotted world map in the background"></div>

    <div class="brand">
      <span class="brand__dot"></span>
      <div class="brand__text">
        <div class="brand__name">KORVEN</div>
        <div class="brand__tag">DIGITAL SOLUTIONS</div>
      </div>
    </div>

    <p class="website">www.digital.korven-beispiel.eu</p>
  </section>

</body>
</html>
```